2-Sided Checklist

I need well designed checklist. This will be handed out by insurance agents, wealth managers, and estate planners as a way to instruct their clients on organization and planning. The checklist features and To Do list on one side and an advertisement for services on the other. The checklist should be easy to read, showcase a professional design, and feature our logo on the back.

I've included the checklist copy and logo in the uploaded files.

Target Market(s)

Insurance Agents and Wealth Managers will hand these out to their clients (typically 40-65 y/o)

Requirements
Must have
• Must include the logo and text
• Must be in MS Word for updates and printability

```html
<!DOCTYPE html>
<html lang="en">
<head>
<meta charset="utf-8">
<title>Keystead – Life Document Checklist</title>
<link rel="stylesheet" href="https://fonts.googleapis.com/css2?family=Arimo:wght@400;700&family=Noto+Sans:wght@400;700&display=swap">
<style>
  :root {
    --backdrop: #1b1b1b;
    --card-top: #e8f8fb;
    --card-mid: #dff4f8;
    --card-bottom: #cdf3f7;
    --brand-grey: #4b4e52;
    --brand-dot: #3aa0e8;
    --title-red: #ff2a10;
    --ink: #111111;
    --item-text: #1c1c1c;
    --box-line: #b9c4c8;
    --box-fill: #f4fbfc;
    --rule: #333333;
  }
  html, body {
    margin: 0;
    padding: 0;
    width: 1200px;
    height: 2183px;
    overflow: hidden;
    background: var(--backdrop);
  }
  .checklist-card {
    position: absolute;
    left: 126px;
    top: 140px;
    width: 950px;
    height: 1903px;
    overflow: hidden;
    background: linear-gradient(170deg, var(--card-top) 0%, #ffffff 22%, var(--card-mid) 55%, var(--card-bottom) 100%);
    font-family: "Noto Sans", "Verdana", sans-serif;
  }
  .card-waves {
    position: absolute;
    inset: 0;
    width: 100%;
    height: 100%;
  }
  .brand {
    position: absolute;
    left: 70px;
    top: 75px;
    display: flex;
    align-items: center;
    gap: 40px;
  }
  .brand-mark {
    width: 145px;
    height: 145px;
    border-radius: 50%;
    background: var(--brand-dot);
  }
  .brand-name {
    font-family: "Arimo", Arial, sans-serif;
    font-weight: 700;
    font-size: 112px;
    line-height: 1;
    color: var(--brand-grey);
    letter-spacing: -1px;
  }
  .checklist-title {
    position: absolute;
    left: 258px;
    top: 232px;
    margin: 0;
    font-family: "Arimo", Arial, sans-serif;
    font-weight: 700;
    font-size: 34px;
    color: var(--title-red);
  }
  .checklist-intro {
    position: absolute;
    left: 260px;
    top: 286px;
    width: 640px;
    margin: 0;
    font-family: "Noto Sans", Verdana, sans-serif;
    font-weight: 700;
    font-size: 23.5px;
    line-height: 31px;
    color: var(--ink);
    letter-spacing: 0.3px;
  }
  .item {
    position: absolute;
    left: 216px;
    width: 666px;
    height: 40px;
    margin-top: -20px;
    display: flex;
    align-items: center;
    font-size: 25.5px;
    color: var(--item-text);
  }
  .item-box {
    flex: none;
    width: 26px;
    height: 26px;
    border: 2px solid var(--box-line);
    border-radius: 5px;
    background: var(--box-fill);
    box-sizing: border-box;
    margin-right: 17px;
  }
  .item-blank {
    flex: 1;
    align-self: flex-end;
    height: 8px;
    border-bottom: 2px solid var(--rule);
  }
</style>
</head>
<body>
  <main class="checklist-card">
    <svg class="card-waves" viewBox="0 0 950 1903" preserveAspectRatio="none" aria-hidden="true">
      <path d="M0 0 C 250 300, 700 200, 950 60 L950 0 Z" fill="#ffffff" opacity="0.55"/>
      <path d="M0 520 C 300 380, 650 700, 950 520 L950 760 C 650 900, 300 640, 0 820 Z" fill="#ffffff" opacity="0.35"/>
      <path d="M0 1250 C 350 1050, 600 1500, 950 1300 L950 1903 L0 1903 Z" fill="#c5f0f5" opacity="0.35"/>
    </svg>

    <header class="brand">
      <div class="brand-mark"></div>
      <div class="brand-name">Keystead</div>
    </header>

    <h1 class="checklist-title">Life Document Checklist</h1>
    <p class="checklist-intro">Everyone should have the following information securely stored and available to family members and trusted advisors.</p>

    <section class="checklist-group" aria-label="Insurance">
      <div class="item" style="top:414px"><span class="item-box"></span>Insurance</div>
      <div class="item" style="top:470px"><span class="item-box"></span>Life</div>
      <div class="item" style="top:526px"><span class="item-box"></span>Health</div>
      <div class="item" style="top:581px"><span class="item-box"></span>Home Owners</div>
      <div class="item" style="top:638px"><span class="item-box"></span>Automotive</div>
      <div class="item" style="top:694px"><span class="item-box"></span>Umbrella</div>
      <div class="item" style="top:749px"><span class="item-box"></span>Final Expenses</div>
      <div class="item" style="top:807px"><span class="item-box"></span><span class="item-blank"></span></div>
      <div class="item" style="top:864px"><span class="item-box"></span><span class="item-blank"></span></div>
    </section>

    <section class="checklist-group" aria-label="Health and accident">
      <div class="item" style="top:951px"><span class="item-box"></span>Health/Accident</div>
      <div class="item" style="top:997px"><span class="item-box"></span>Medical History</div>
      <div class="item" style="top:1044px"><span class="item-box"></span>Medications</div>
      <div class="item" style="top:1091px"><span class="item-box"></span>Allergies</div>
      <div class="item" style="top:1137px"><span class="item-box"></span>Advanced Directives</div>
      <div class="item" style="top:1184px"><span class="item-box"></span>Medical Contacts (GP, specialists)</div>
      <div class="item" style="top:1231px"><span class="item-box"></span>Emergency Contacts (family, friends)</div>
      <div class="item" style="top:1278px"><span class="item-box"></span><span class="item-blank"></span></div>
      <div class="item" style="top:1324px"><span class="item-box"></span><span class="item-blank"></span></div>
    </section>

    <section class="checklist-group" aria-label="Legacy">
      <div class="item" style="top:1408px"><span class="item-box"></span>Legacy</div>
      <div class="item" style="top:1455px"><span class="item-box"></span>Final Will</div>
      <div class="item" style="top:1501px"><span class="item-box"></span>Trust</div>
      <div class="item" style="top:1548px"><span class="item-box"></span>Burial Instructions</div>
      <div class="item" style="top:1595px"><span class="item-box"></span>Digital Footprint</div>
      <div class="item" style="top:1641px"><span class="item-box"></span>Financial Accounts</div>
      <div class="item" style="top:1688px"><span class="item-box"></span>Property Investments</div>
      <div class="item" style="top:1735px"><span class="item-box"></span>Business Ownership</div>
      <div class="item" style="top:1781px"><span class="item-box"></span><span class="item-blank"></span></div>
      <div class="item" style="top:1828px"><span class="item-box"></span><span class="item-blank"></span></div>
    </section>
  </main>
</body>
</html>
```